TBranwell executive consulting

We need a basic clean website for executive consulting. Rosalind is the previos CIO for bluecrest airways and currently supports several technology companies with innovation and transformation.

Target Market(s)

C level technology and CIO training

Industry/Entity Type

Technology and travel industry

Coding

Coded - Design and coding required

Number of Pages Required

3 page

Font styles to use
Sans Serif

Colors
0054AA
0677BA
7BADD7
CADEEF
E8F1F8
0094D4
00A9DD
6FCCEA
C7EBF8
E9F6FB

Requirements
Must have
• Home page, about us, services social media links

```html
<!DOCTYPE html>
<html lang="en">
<head>
<meta charset="utf-8">
<title>TBranwell Executive Consulting</title>
<link href="https://fonts.googleapis.com/css2?family=Raleway:wght@400;500;600;700;800&family=Lora:wght@400&family=Montserrat:wght@400;500;600&display=swap" rel="stylesheet">
<style>
:root{
  --teal:#00A9DD;
  --teal-deep:#0094D4;
  --ink:#101418;
  --dark:#14222b;
  --grey-bg:#f4f4f4;
  --text:#3d3d3d;
  --white:#ffffff;
}
*{box-sizing:border-box;margin:0;padding:0}
html,body{width:1200px;height:4468px;overflow:hidden;background:var(--white)}
body{position:relative;font-family:'Montserrat',sans-serif;color:var(--text)}
.abs{position:absolute}
.display{font-family:'Raleway',sans-serif;font-variant:small-caps}
.btn{position:absolute;display:flex;align-items:center;justify-content:center;border-radius:30px;color:var(--white);font-family:'Raleway',sans-serif;font-variant:small-caps;font-weight:600;font-size:22px;letter-spacing:.5px;background:linear-gradient(90deg,var(--teal) 0%,var(--teal-deep) 40%,var(--dark) 100%)}

/* header + hero */
.hero{position:absolute;left:0;top:0;width:1200px;height:628px;background:var(--white);overflow:hidden}
.hero-photo{position:absolute;left:420px;top:0;width:780px;height:628px;background:linear-gradient(90deg,#ffffff 0%,#efe9e3 22%,#d8c7b6 48%,#b9a48f 72%,#8f8a86 100%)}
.brand{position:absolute;left:111px;top:34px;font-family:'Raleway',sans-serif;font-size:34px;font-weight:700;color:var(--dark);display:flex;align-items:center;gap:10px}
.brand-dot{width:16px;height:16px;border-radius:50%;background:var(--teal)}
.nav{position:absolute;top:44px;font-family:'Lora',serif;font-size:17px;color:#222}
.nav.active{color:var(--teal)}
.hero-kicker{left:111px;top:200px;font-family:'Raleway',sans-serif;font-variant:small-caps;font-weight:500;font-size:44px;color:#1a1a1a}
.hero-name{left:111px;top:248px;font-family:'Raleway',sans-serif;font-variant:small-caps;font-size:58px;font-weight:700;color:var(--teal);white-space:nowrap}
.hero-text{left:111px;top:324px;width:470px;font-size:15px;line-height:23px;color:#333}
.scroll{left:44px;top:275px;width:28px;height:100px;writing-mode:vertical-rl;transform:rotate(180deg);font-family:'Lora',serif;font-size:16px;color:#222;text-align:center}
.dot{position:absolute;top:580px;width:16px;height:16px;border-radius:50%;background:var(--white)}

/* about */
.about-ring{left:122px;top:754px;width:450px;height:622px;background:var(--white);border-radius:0 0 225px 225px}
.about-photo{left:137px;top:754px;width:420px;height:595px;border-radius:0 0 210px 210px;background:linear-gradient(180deg,#cfc8c0 0%,#9c8f85 45%,#3a3b44 100%)}
.h-about{left:638px;top:780px;font-family:'Raleway',sans-serif;font-weight:800;font-size:44px;color:var(--ink);text-transform:uppercase}
.about-text{left:638px;top:866px;width:440px;font-size:15px;line-height:25.7px;color:#444}

/* services */
.services-bg{left:0;top:1269px;width:1200px;height:1388px;background:var(--grey-bg)}
.section-title{position:absolute;left:0;width:1200px;display:flex;align-items:center;justify-content:center;gap:14px;font-family:'Raleway',sans-serif;font-weight:800;font-size:46px;color:var(--ink);text-transform:uppercase}
.card{position:absolute;width:311px;height:451px;background:var(--white);border-radius:6px 6px 150px 150px;overflow:hidden}
.card.featured{border:6px solid var(--teal)}
.card-img{position:absolute;left:8px;top:6px;right:8px;height:182px}
.card-icon{position:absolute;left:50%;top:152px;width:72px;height:72px;margin-left:-36px;border-radius:50%;background:var(--white);border:5px solid var(--teal);display:flex;align-items:center;justify-content:center}
.card-title{position:absolute;left:8px;right:8px;top:240px;text-align:center;font-family:'Raleway',sans-serif;font-variant:small-caps;font-weight:600;font-size:22px;line-height:30px;color:#1b1b1b}
.card-desc{position:absolute;left:24px;right:24px;top:300px;height:88px;overflow:hidden;text-align:center;font-size:12.5px;line-height:21.5px;font-weight:500;color:#1b1b1b}
.card-arrow{position:absolute;left:50%;bottom:18px;margin-left:-19px}

/* testimonials */
.testi-bg{left:0;top:2657px;width:1200px;height:556px;background:linear-gradient(90deg,#0ea0d0 0%,#1aa7d6 50%,#0d9bcb 100%)}
.testi-title{color:var(--white)}
.testi-text{left:180px;top:2800px;width:840px;text-align:center;font-size:15.5px;line-height:26px;color:#f2fbff}
.testi-text p{margin-bottom:26px}
.avatar{left:578px;top:3075px;width:44px;height:44px;border-radius:50%;background:linear-gradient(180deg,#c9d2d8,#5a6670);border:2px solid var(--white)}
.testi-name{left:0;top:3126px;width:1200px;text-align:center;font-style:italic;font-size:15px;color:#e8f7fd}

/* contact */
.footer-bg{left:0;top:3832px;width:1200px;height:636px;background:#000}
.form-panel{left:113px;top:3442px;width:974px;height:508px;background:var(--white);box-shadow:0 0 6px rgba(0,0,0,.12)}
.form-bar{position:absolute;left:0;top:0;width:974px;height:47px;background:var(--teal);color:var(--white);font-family:'Raleway',sans-serif;font-variant:small-caps;font-weight:600;font-size:21px;display:flex;align-items:center;justify-content:center}
.field{position:absolute;border:1px solid #cfcfcf;font-family:'Lora',serif;font-size:16px;color:#444;padding:13px 12px}

/* footer */
.f-brand{left:114px;top:4130px;font-family:'Raleway',sans-serif;font-size:58px;font-weight:700;color:var(--teal)}
.f-head{position:absolute;top:4040px;font-family:'Raleway',sans-serif;font-variant:small-caps;font-weight:600;font-size:26px;color:var(--white)}
.f-rule{position:absolute;top:4082px;height:3px;background:var(--teal)}
.f-link{position:absolute;left:502px;font-size:17px;font-weight:600;color:var(--white)}
.email{left:801px;top:4124px;width:286px;height:59px;border-radius:30px;background:var(--white);font-family:'Lora',serif;font-size:16px;color:#555;padding:19px 16px}
.social-label{left:801px;top:4214px;font-size:15px;font-weight:600;color:var(--white)}
.social{position:absolute;top:4246px;width:38px;height:38px;border-radius:50%;border:2px solid var(--teal);background:transparent}
.copy{left:0;top:4396px;width:1200px;text-align:center;font-size:16px;font-weight:600;color:var(--white)}
</style>
</head>
<body>

<!-- HERO -->
<section class="hero">
  <div class="hero-photo" role="img" aria-label="Photo of two businesswomen reviewing work on a laptop"></div>
  <div class="brand"><span class="brand-dot"></span>TBranwell</div>
  <span class="nav active" style="left:423px">Home</span>
  <span class="nav" style="left:524px">About Us</span>
  <span class="nav" style="left:647px">Our Services</span>
  <span class="nav" style="left:800px">Testimonials</span>
  <span class="nav" style="left:952px">Contact Us</span>
  <div class="abs hero-kicker">Welcome To</div>
  <div class="abs hero-name">Rosalind Branwell</div>
  <p class="abs hero-text">including 20 transformative years at Bluecrest Airways. As the Senior Vice President of Technology (CIO), Rosalind spearheaded</p>
  <a class="btn" style="left:111px;top:402px;width:170px;height:55px">Let’s Talk</a>
  <div class="abs scroll">Scroll Down</div>
  <svg class="abs" style="left:50px;top:403px" width="18" height="38" viewBox="0 0 18 38"><path d="M9 0v34M2 27l7 9 7-9" stroke="#111" stroke-width="3" fill="none"/></svg>
  <span class="dot" style="left:555px"></span>
  <span class="dot" style="left:580px"></span>
  <span class="dot" style="left:604px;background:var(--teal)"></span>
  <span class="dot" style="left:628px"></span>
</section>

<!-- ABOUT -->
<section>
  <div class="abs services-bg"></div>
  <div class="abs about-ring"></div>
  <div class="abs about-photo" role="img" aria-label="Portrait of Rosalind Branwell in a business suit"></div>
  <h2 class="abs h-about">About Us</h2>
  <svg class="abs" style="left:636px;top:838px" width="180" height="12" viewBox="0 0 180 12"><polygon points="0,2 180,0 180,10 0,12" fill="var(--teal)"/></svg>
  <p class="abs about-text">Rosalind Branwell is a seasoned leader with a remarkable 40-year career in the travel industry, including 20 transformative years at Bluecrest Airways. As the Senior Vice President of Technology (CIO), Rosalind spearheaded some of the company’s most significant technological and strategic transformations, helping Bluecrest Airways stay at the forefront of innovation in the competitive travel market. Her work bridged the gap between business strategy and technology, driving measurable success and resilience.</p>
  <a class="btn" style="left:638px;top:1135px;width:196px;height:55px">Learn More</a>
</section>

<!-- SERVICES -->
<section>
  <h2 class="section-title" style="top:1412px">
    <svg width="72" height="14" viewBox="0 0 72 14"><polygon points="0,5 72,0 72,14" fill="var(--teal)"/></svg>
    Our Services
    <svg width="72" height="14" viewBox="0 0 72 14"><polygon points="0,0 72,5 0,14" fill="var(--teal)"/></svg>
  </h2>

  <article class="card" style="left:114px;top:1509px">
    <div class="card-img" role="img" aria-label="Photo of a mentoring group in an office" style="background:linear-gradient(135deg,#e3e6e8,#8c939a 60%,#4a4f56)"></div>
    <div class="card-icon"><svg width="34" height="34" viewBox="0 0 34 34" fill="none" stroke="#333" stroke-width="2"><circle cx="17" cy="8" r="4"/><circle cx="7" cy="24" r="3.5"/><circle cx="27" cy="24" r="3.5"/><path d="M17 12v6M7 18h20M7 18v2M27 18v2"/></svg></div>
    <h3 class="card-title">Leadership<br>Mentorship</h3>
    <p class="card-desc">Personalized coaching for IT leaders to develop strategic decision-making, emotional intelligence, and resilience. Mentorship programs for aspiring</p>
    <svg class="card-arrow" width="38" height="38" viewBox="0 0 38 38" fill="none" stroke="#222" stroke-width="2"><circle cx="19" cy="19" r="17"/><path d="M11 19h16M21 13l6 6-6 6"/></svg>
  </article>

  <article class="card featured" style="left:447px;top:1509px">
    <div class="card-img" role="img" aria-label="Photo of a hand with glowing technology network graphics" style="left:2px;right:2px;top:0;background:linear-gradient(135deg,#0b2547,#1c5c9a 50%,#0a1a33)"></div>
    <div class="card-icon" style="top:146px"><svg width="34" height="34" viewBox="0 0 34 34" fill="none" stroke="#333" stroke-width="2"><rect x="5" y="7" width="24" height="16" rx="2"/><path d="M12 28h10M17 23v5"/><circle cx="17" cy="15" r="4"/></svg></div>
    <h3 class="card-title" style="top:234px">Technology Strategy<br>Development</h3>
    <p class="card-desc" style="top:294px">Creating IT strategies aligned with overall business goals.<br>Advising on IT infrastructure modernization and innovation</p>
    <svg class="card-arrow" style="bottom:12px" width="38" height="38" viewBox="0 0 38 38" fill="none" stroke="#222" stroke-width="2"><circle cx="19" cy="19" r="17"/><path d="M11 19h16M21 13l6 6-6 6"/></svg>
  </article>

  <article class="card" style="left:780px;top:1509px">
    <div class="card-img" role="img" aria-label="Photo of professionals working with digital screens" style="background:linear-gradient(135deg,#2f5f8f,#1d4f86 50%,#8fb3d6)"></div>
    <div class="card-icon"><svg width="34" height="34" viewBox="0 0 34 34" fill="none" stroke="#333" stroke-width="2"><circle cx="17" cy="17" r="10"/><circle cx="17" cy="17" r="3"/><path d="M17 3v4M17 27v4M3 17h4M27 17h4"/></svg></div>
    <h3 class="card-title">Digital Transformation<br>Consulting</h3>
    <p class="card-desc">Assessing current digital maturity and identifying opportunities for improvement.<br>Designing and implementing digital</p>
    <svg class="card-arrow" width="38" height="38" viewBox="0 0 38 38" fill="none" stroke="#222" stroke-width="2"><circle cx="19" cy="19" r="17"/><path d="M11 19h16M21 13l6 6-6 6"/></svg>
  </article>

  <article class="card" style="left:114px;top:2008px">
    <div class="card-img" role="img" aria-label="Photo of a businessman with a tablet and digital graphics" style="background:linear-gradient(135deg,#dfe4e8,#7a8896 55%,#26384a)"></div>
    <div class="card-icon"><svg width="34" height="34" viewBox="0 0 34 34" fill="none" stroke="#333" stroke-width="2"><path d="M4 18l7-7 6 4 6-4 7 7-10 9z"/><path d="M11 11l6 6"/></svg></div>
    <h3 class="card-title">IT-Business Partnership<br>Development</h3>
    <p class="card-desc">Workshops and training sessions to strengthen collaboration between IT and business units.</p>
    <svg class="card-arrow" width="38" height="38" viewBox="0 0 38 38" fill="none" stroke="#222" stroke-width="2"><circle cx="19" cy="19" r="17"/><path d="M11 19h16M21 13l6 6-6 6"/></svg>
  </article>

  <article class="card" style="left:447px;top:2008px">
    <div class="card-img" role="img" aria-label="Photo of hands arranging glowing gears" style="background:linear-gradient(135deg,#1b2a3a,#c26a2a 50%,#2a4d73)"></div>
    <div class="card-icon"><svg width="34" height="34" viewBox="0 0 34 34" fill="none" stroke="#333" stroke-width="2"><circle cx="17" cy="17" r="9"/><circle cx="17" cy="17" r="3.5"/><path d="M17 4v4M17 26v4M4 17h4M26 17h4M8 8l3 3M23 23l3 3M26 8l-3 3M8 26l3-3"/></svg></div>
    <h3 class="card-title">Organizational<br>Change Management</h3>
    <p class="card-desc">Strategies for fostering a culture of adaptability and innovation.<br>Communication frameworks for large-scale IT or organizational</p>
    <svg class="card-arrow" width="38" height="38" viewBox="0 0 38 38" fill="none" stroke="#222" stroke-width="2"><circle cx="19" cy="19" r="17"/><path d="M11 19h16M21 13l6 6-6 6"/></svg>
  </article>

  <article class="card" style="left:780px;top:2008px">
    <div class="card-img" role="img" aria-label="Photo of engineers reviewing a project in a lab" style="background:linear-gradient(135deg,#e6e8ea,#9aa3ab 50%,#3d4753)"></div>
    <div class="card-icon"><svg width="34" height="34" viewBox="0 0 34 34" fill="none" stroke="#333" stroke-width="2"><rect x="5" y="6" width="24" height="20" rx="2"/><path d="M5 11h24M9 16h8M9 20h12"/></svg></div>
    <h3 class="card-title">Program and Project<br>Oversight</h3>
    <p class="card-desc">Assessing current digital maturity and identifying opportunities for improvement.<br>Designing and implementing digital</p>
    <svg class="card-arrow" width="38" height="38" viewBox="0 0 38 38" fill="none" stroke="#222" stroke-width="2"><circle cx="19" cy="19" r="17"/><path d="M11 19h16M21 13l6 6-6 6"/></svg>
  </article>

  <a class="btn" style="left:458px;top:2525px;width:284px;height:55px">View All Services</a>
</section>

<!-- TESTIMONIALS -->
<section>
  <div class="abs testi-bg" role="img" aria-label="Faded photo of a team meeting under a blue overlay"></div>
  <h2 class="section-title testi-title" style="top:2715px">
    <svg width="72" height="14" viewBox="0 0 72 14"><polygon points="0,7 72,0 72,14" fill="#0a0a0a"/></svg>
    <span style="margin:0 20px">Testimonials</span>
    <svg width="72" height="14" viewBox="0 0 72 14"><polygon points="0,0 72,7 0,14" fill="#0a0a0a"/></svg>
  </h2>
  <div class="abs testi-text">
    <p>Rosalind is a decisive and fair leader who exemplifies strength, wisdom, and empathy. She always possesses a clear vision for the future and is willing to make bold decisions which are grounded in data, expertise, and intuition while remaining open to diverse perspectives.</p>
    <p>Rosalind’s leadership style fosters an inclusive environment where every voice matters, empowering her team to excel and innovate. She was able to balance ambition with humanity and succeeded in prioritizing the well-being of her people, ensuring they feel valued and supported.</p>
    <p>In times of uncertainty her unwavering confidence and fairness inspire trust, driving the organization forward with resilience and integrity.</p>
  </div>
  <div class="abs avatar" role="img" aria-label="Portrait of Daniel Foster"></div>
  <div class="abs testi-name">Daniel Foster, <b>CEO Norvale</b></div>
</section>

<!-- CONTACT -->
<section>
  <div class="abs footer-bg"></div>
  <h2 class="section-title" style="top:3326px">
    <svg width="72" height="14" viewBox="0 0 72 14"><polygon points="0,5 72,0 72,14" fill="var(--teal)"/></svg>
    <span style="margin:0 14px">Contact Us</span>
    <svg width="72" height="14" viewBox="0 0 72 14"><polygon points="0,0 72,5 0,14" fill="var(--teal)"/></svg>
  </h2>
  <div class="abs form-panel">
    <div class="form-bar">Let’s Talk The TBranwell</div>
    <svg class="abs" style="left:467px;top:46px" width="40" height="20" viewBox="0 0 40 20"><polygon points="0,0 40,0 20,20" fill="var(--teal)"/></svg>
    <div class="field" style="left:27px;top:106px;width:445px;height:48px">Name</div>
    <div class="field" style="left:501px;top:106px;width:444px;height:48px">Phone</div>
    <div class="field" style="left:27px;top:176px;width:445px;height:46px">Email</div>
    <div class="field" style="left:501px;top:176px;width:444px;height:46px">Subject</div>
    <div class="field" style="left:27px;top:244px;width:918px;height:145px">Message</div>
    <a class="btn" style="left:399px;top:423px;width:176px;height:50px">Send Now</a>
  </div>
</section>

<!-- FOOTER -->
<footer>
  <div class="abs f-brand">TBranwell</div>
  <div class="f-head" style="left:494px">Quick Links</div>
  <div class="f-rule" style="left:494px;width:98px"></div>
  <a class="f-link" style="top:4114px">Home</a>
  <a class="f-link" style="top:4147px">About Us</a>
  <a class="f-link" style="top:4181px">Our Services</a>
  <a class="f-link" style="top:4214px">Testimonials</a>
  <a class="f-link" style="top:4247px">Contact Us</a>
  <div class="f-head" style="left:798px">Keep In Touch</div>
  <div class="f-rule" style="left:801px;width:92px"></div>
  <div class="abs email">Enter Email</div>
  <svg class="abs" style="left:1029px;top:4133px" width="44" height="44" viewBox="0 0 44 44"><circle cx="22" cy="22" r="21" fill="#bfbfbf"/><path d="M12 22l20-9-7 19-3-7z" fill="#fff"/></svg>
  <div class="abs social-label">Follow Us</div>
  <a class="social" style="left:801px" aria-label="Social profile one"></a>
  <a class="social" style="left:851px" aria-label="Social profile two"></a>
  <a class="social" style="left:901px" aria-label="Social profile three"></a>
  <a class="social" style="left:951px" aria-label="Social profile four"></a>
  <div class="abs" style="left:111px;top:4342px;width:977px;height:2px;background:var(--white)"></div>
  <div class="abs copy">Copyrights 2025 Company Name All Rights Reserved</div>
</footer>

</body>
</html>
```